Brightmere Foot Works patient advertisement flyer

We need a flyer for a new fungal nail treatment clinic called brightmere foot works. We require a flyer/brochure that advertises our clinic and what we do (please find attached a document that has the information we would like included - we are completely open to the designer structuring the information how they see fit so long as it encompasses the information provided). We also have a booklet that we give to patients on their initial consult (which I have attached to give you an idea of the colour schemes /design that we are already using and we would like our brochure to align with this booklet). I have also attached our logo for use in the brochure. Finally, I have attached a copy of our cold laser brochure and associated pictures - ideally we would like to capture something similar to this brochure and have a picture of the laser somewhere on the brochure. We would like our brochure to communicate professional but be sleek, modern and have a minimalist look.

Can we please make these tri fold outs please like a brochure format 😊

```html
<!DOCTYPE html>
<html lang="en">
<head>
<meta charset="utf-8">
<title>Brightmere Foot Works – Tri-fold Brochure</title>
<link rel="stylesheet" href="https://fonts.googleapis.com/css2?family=Arimo:ital,wght@0,400;0,700;1,400;1,700&family=Archivo+Black&display=swap">
<style>
  :root{
    --blue:#3b69bd;
    --blue-light:#6a93dc;
    --navy:#1f3890;
    --navy-deep:#182c7e;
    --ink:#2a2a2a;
    --paper:#ffffff;
    --backdrop:#e6e7ea;
    --skin-1:#f3d9cc;
    --skin-2:#e8bfae;
    --mat:#efe6d8;
  }
  *{box-sizing:border-box;margin:0;padding:0}
  html,body{width:1200px;height:2658px;overflow:hidden}
  body{background:var(--backdrop);position:relative;font-family:"Arimo",Arial,sans-serif;color:var(--ink)}

  .sheet{position:absolute;background:var(--paper);box-shadow:0 10px 28px rgba(0,0,0,.18);overflow:hidden}
  .cover-solo{left:420px;top:70px;width:360px;height:764px}
  .spread{left:40px;width:1120px;height:792px;display:flex}
  .spread--outside{top:914px}
  .spread--inside{top:1786px}
  .panel{position:relative;width:33.333%;height:100%;overflow:hidden}
  .panel + .panel{border-left:1px solid rgba(0,0,0,.06)}

  .wave{position:absolute;left:0;bottom:0;width:100%;display:block}

  /* wordmark: plain text with one square */
  .brand{display:flex;align-items:center;justify-content:center;gap:10px}
  .brand-square{width:16px;height:16px;background:currentColor;flex:none}
  .brand-name{font-family:"Arimo",Arial,sans-serif;font-weight:700;font-size:24px;line-height:1.2;white-space:nowrap}

  /* cover */
  .cover{position:absolute;inset:0;background:var(--paper)}
  .cover__band{position:absolute;left:0;top:0;width:100%;height:28%;background:var(--blue);display:flex;align-items:center;justify-content:center}
  .cover__band .brand{color:var(--paper)}
  .cover__photo{position:absolute;left:0;top:28%;width:100%;height:54%;background:linear-gradient(160deg,var(--mat) 0%,var(--skin-1) 45%,var(--skin-2) 100%)}
  .cover__wave{height:30%}
  .cover__web{position:absolute;left:0;right:0;bottom:5%;text-align:center;color:var(--paper);font-weight:700;font-size:17px;letter-spacing:.3px;transform:rotate(-6deg)}

  /* outside left */
  .tiptoe-photo{position:absolute;left:0;top:0;width:100%;height:42%;background:linear-gradient(180deg,#f6efe9 0%,var(--skin-1) 60%,#f7f3ef 100%)}
  .tag{position:absolute;background:var(--blue);color:var(--paper);font-family:"Archivo Black",sans-serif;text-transform:uppercase;line-height:1.05;padding:8px 16px 8px 20px;clip-path:polygon(0 0,100% 0,94% 100%,0 100%)}
  .tag--advantage{left:0;top:37%;font-size:19px;font-style:italic;width:62%}
  .advantages{position:absolute;left:28px;right:26px;top:52%;list-style:none;display:flex;flex-direction:column;gap:11px}
  .advantages li{position:relative;padding-left:20px;font-size:11.5px;font-weight:700;font-style:italic;text-transform:uppercase;line-height:1.35}
  .advantages li::before{content:"";position:absolute;left:0;top:3px;width:8px;height:8px;border-radius:50%;background:var(--blue)}
  .panel__wave-low{height:24%}

  /* outside middle */
  .contact{position:absolute;left:0;right:0;top:16%;text-align:center;padding:0 30px;color:var(--ink)}
  .contact .brand{color:var(--navy);margin-bottom:44px}
  .contact__lead{font-style:italic;font-size:13px;line-height:1.45;margin-bottom:36px}
  .contact__clinic{font-family:"Archivo Black",sans-serif;font-size:21px;line-height:1.1;text-transform:uppercase;margin-bottom:12px}
  .contact__line{font-style:italic;font-size:12.5px;line-height:1.65}

  /* inside left */
  .about-photo{position:absolute;left:0;top:0;width:44%;height:17%;background:linear-gradient(135deg,#e4c0b0 0%,#c98fa7 60%,#f1e3e6 100%)}
  .tag--about{left:44%;top:8%;font-size:16px;padding:7px 18px 7px 14px;width:54%}
  .body-copy{position:absolute;left:30px;right:30px;font-size:10.5px;line-height:1.42}
  .body-copy p + p{margin-top:12px}
  .about-copy{top:22%}

  /* inside middle */
  .laser-photo{position:absolute;left:0;top:0;width:100%;height:56%;background:linear-gradient(150deg,#f2f2f4 0%,#d9d6dc 35%,#c24a9c 55%,#e7b6a2 75%,#eeeef0 100%)}
  .laser-field{position:absolute;left:0;right:0;top:52%;bottom:0;background:var(--navy-deep)}
  .laser-field__curve{position:absolute;left:0;top:-40px;width:100%;height:60px}
  .laser-copy{top:58%;color:var(--paper)}

  /* inside right */
  .results{position:absolute;inset:0;background:var(--navy-deep)}
  .ribbon{position:absolute;left:24px;background:var(--blue);color:var(--paper);font-family:"Archivo Black",sans-serif;font-size:20px;padding:6px 40px 6px 16px;clip-path:polygon(0 0,100% 0,90% 50%,100% 100%,0 100%)}
  .ribbon--before{top:5%}
  .ribbon--after{top:36%}
  .result-photo{position:absolute;left:60px;right:24px;height:22%;border:4px solid var(--paper)}
  .result-photo--before{top:11%;background:linear-gradient(135deg,#e9dccc 0%,#b8a060 50%,#efe9df 100%)}
  .result-photo--after{top:42%;background:linear-gradient(135deg,#e9dccc 0%,#c9a58a 50%,#f1ece4 100%)}
  .results-copy{top:70%;color:var(--paper)}
</style>
</head>
<body>

  <section class="sheet cover-solo">
    <div class="cover">
      <div class="cover__band">
        <div class="brand"><span class="brand-square"></span><span class="brand-name">Brightmere Foot Works</span></div>
      </div>
      <div class="cover__photo" role="img" aria-label="Photo of manicured hands resting on bare feet with a pink lily on a woven mat"></div>
      <svg class="wave cover__wave" viewBox="0 0 100 100" preserveAspectRatio="none" aria-hidden="true">
        <path d="M0 42 Q45 2 100 8 L100 100 L0 100Z" fill="var(--blue-light)"/>
        <path d="M0 58 Q50 22 100 28 L100 100 L0 100Z" fill="var(--navy)"/>
        <path d="M0 78 Q50 46 100 52 L100 100 L0 100Z" fill="var(--blue)"/>
      </svg>
      <div class="cover__web">www.brightmerefootworks.co.nz</div>
    </div>
  </section>

  <section class="sheet spread spread--outside">
    <div class="panel">
      <div class="tiptoe-photo" role="img" aria-label="Photo of bare feet standing on tiptoe"></div>
      <div class="tag tag--advantage">The Clearpath Advantage</div>
      <ul class="advantages">
        <li>No pain, no downtime and no risk</li>
        <li>6.1mm new clear nail growth at 6 months</li>
        <li>No dangerous smoke plumes</li>
        <li>FDA market cleared for new clear nail growth at months</li>
        <li>89% of patients respond</li>
      </ul>
      <svg class="wave panel__wave-low" viewBox="0 0 100 100" preserveAspectRatio="none" aria-hidden="true">
        <path d="M0 20 Q40 70 100 55 L100 100 L0 100Z" fill="var(--blue-light)"/>
        <path d="M0 40 Q45 85 100 70 L100 100 L0 100Z" fill="var(--blue)"/>
      </svg>
    </div>

    <div class="panel">
      <div class="contact">
        <div class="brand"><span class="brand-square"></span><span class="brand-name">Brightmere Foot Works</span></div>
        <p class="contact__lead">To be rid of your unsightly fungal nails for good come and discuss with our clinicians the best treatment option for you</p>
        <p class="contact__clinic">Harrowgate Clinic<br>Pharmacy</p>
        <p class="contact__line">14 Calder Lane, Westbrook Central</p>
        <p class="contact__line">Phone: (07) 555 0142</p>
        <p class="contact__line">Email: reception@brightmerefootworks.co.nz</p>
        <p class="contact__line">www.brightmerefootworks.co.nz</p>
      </div>
      <svg class="wave panel__wave-low" viewBox="0 0 100 100" preserveAspectRatio="none" aria-hidden="true">
        <path d="M0 55 Q50 85 100 25 L100 100 L0 100Z" fill="var(--blue-light)"/>
        <path d="M0 70 Q55 95 100 45 L100 100 L0 100Z" fill="var(--blue)"/>
      </svg>
    </div>

    <div class="panel">
      <div class="cover">
        <div class="cover__band">
          <div class="brand"><span class="brand-square"></span><span class="brand-name">Brightmere Foot Works</span></div>
        </div>
        <div class="cover__photo" role="img" aria-label="Photo of manicured hands resting on bare feet with a pink lily on a woven mat"></div>
        <svg class="wave cover__wave" viewBox="0 0 100 100" preserveAspectRatio="none" aria-hidden="true">
          <path d="M0 42 Q45 2 100 8 L100 100 L0 100Z" fill="var(--blue-light)"/>
          <path d="M0 58 Q50 22 100 28 L100 100 L0 100Z" fill="var(--navy)"/>
          <path d="M0 78 Q50 46 100 52 L100 100 L0 100Z" fill="var(--blue)"/>
        </svg>
        <div class="cover__web">www.brightmerefootworks.co.nz</div>
      </div>
    </div>
  </section>

  <section class="sheet spread spread--inside">
    <div class="panel">
      <div class="about-photo" role="img" aria-label="Photo of a foot being treated by a clinician in gloves"></div>
      <div class="tag tag--about">About Brightmere Foot Works</div>
      <div class="body-copy about-copy">
        <p>At Brightmere Foot Works, we are your experts at treating fungal nail infections and understand that fungal nail infections can reduce your confidence to wearing open toe shoes and bare feet due to thickened, yellow or irregularly shaped nails. We also understand that getting rid of a fungal nail infection can be extremely difficult involving treatments that are laborious, time consuming and usually unsuccessful.</p>
        <p>Brightmere Foot Works is a new and innovative clinic specifically looking at the diagnosis and treatment of fungal nails, bringing the latest technology to Westbrook to treat fungal nail infections. Our clinicians were frustrated by the lack of successful and safe treatments available, therefore, Brightmere Foot Works have bought our patients the latest in fungal nail treatment which is cold laser therapy. Cold laser therapy provides a simple, safe, and effective up to 87% success rate as well as being a pain free way of treating fungal nail infections.</p>
        <p>Our clinicians here at Brightmere Foot Works will take the time to diagnose and discuss the right treatment for you. We have comprehensive treatment packages that will be tailored to your needs. These include a combination of laser, topical, oral, and surgical options. Explore our website to discover your fungal nail solution.</p>
      </div>
      <svg class="wave panel__wave-low" viewBox="0 0 100 100" preserveAspectRatio="none" aria-hidden="true">
        <path d="M0 50 Q50 70 100 45 L100 100 L0 100Z" fill="var(--blue-light)"/>
        <path d="M0 62 Q50 85 100 60 L100 100 L0 100Z" fill="var(--navy)"/>
      </svg>
    </div>

    <div class="panel">
      <div class="laser-photo" role="img" aria-label="Photo of a foot under a cold laser treatment device glowing pink"></div>
      <div class="laser-field">
        <svg class="laser-field__curve" viewBox="0 0 100 100" preserveAspectRatio="none" aria-hidden="true">
          <path d="M0 100 Q60 20 100 0 L100 100Z" fill="var(--navy-deep)"/>
        </svg>
      </div>
      <div class="body-copy laser-copy">
        <p>Brightmere Foot Works is a new and innovative clinic specifically looking at the diagnosis and treatment of fungal nails, bringing the latest technology to Westbrook to treat fungal nail infections. Our clinicians were frustrated by the lack of successful and safe treatments available, therefore, Brightmere Foot Works have bought our patients the latest in fungal nail treatment which is cold laser therapy. It works through a rotating dual laser system, the violet laser kills the fungus whilst the red laser promotes circulation and your own immune response. Cold laser therapy provides a simple, safe, and effective up to 87% success rate as well as being a pain free way of treating fungal nail infections.</p>
      </div>
      <svg class="wave panel__wave-low" viewBox="0 0 100 100" preserveAspectRatio="none" aria-hidden="true">
        <path d="M0 62 Q50 82 100 58 L100 100 L0 100Z" fill="var(--blue)"/>
        <path d="M0 75 Q50 95 100 72 L100 100 L0 100Z" fill="var(--blue-light)"/>
      </svg>
    </div>

    <div class="panel">
      <div class="results">
        <div class="ribbon ribbon--before">BEFORE</div>
        <div class="result-photo result-photo--before" role="img" aria-label="Close-up photo of a big toe nail with fungal infection before treatment"></div>
        <div class="ribbon ribbon--after">AFTER</div>
        <div class="result-photo result-photo--after" role="img" aria-label="Close-up photo of the same big toe nail growing clear after treatment"></div>
        <div class="body-copy results-copy">
          <p>Our clinicians here at Brightmere Foot Works will take the time to diagnose and discuss the right treatment for you. We have comprehensive treatment packages that will be tailored to your needs. These include a combination of laser, topical, oral, surgical and general nail care options. Explore our website to discover your fungal nail solution.</p>
        </div>
        <svg class="wave panel__wave-low" viewBox="0 0 100 100" preserveAspectRatio="none" aria-hidden="true">
          <path d="M0 60 Q50 75 100 50 L100 100 L0 100Z" fill="var(--blue)"/>
          <path d="M0 74 Q50 92 100 68 L100 100 L0 100Z" fill="var(--blue-light)"/>
        </svg>
      </div>
    </div>
  </section>

</body>
</html>
```